BLQ Business Card

We need a business card that reflect our business, we have put anther business card as an example of what we like but please feel free to do your own thing.

Here are the items to be placed on card

Wade Pelham
Amber Harbor Supply
Mobile: 917-555-4820
Office: 516-555-7164
Fax: 866-555-3291
Email: info@amberharborsupply-example.com
Website: amberharborsupply-example.com

I have added raw files to upload

Wade Pelham
Amber Harbor Supply
Mobile: 917-555-4820
Office: 516-555-7164
Fax: 866-555-3291 

Target Market(s)

Natural product manufactures, and retailers and distributors

Industry/Entity Type

Business

Requirements
Must have
• 1. Logo
2. The colors of the company

```html
<!DOCTYPE html>
<html lang="en">
<head>
<meta charset="utf-8">
<title>BLQ Business Card</title>
<link rel="stylesheet" href="https://fonts.googleapis.com/css2?family=Poppins:wght@400;600;700&display=swap">
<style>
  :root {
    --page: #ece9e4;
    --green: #6cbf3a;
    --green-deep: #58a42c;
    --band: #4a4a4c;
    --band-light: #6a6a6c;
    --paper: #ffffff;
    --ink: #3d3d3f;
    --muted: #555557;
  }
  * { box-sizing: border-box; margin: 0; padding: 0; }
  html, body { width: 1200px; height: 750px; overflow: hidden; }
  body {
    background: var(--page);
    font-family: "Poppins", sans-serif;
    position: relative;
  }
  .card {
    position: absolute;
    top: 215px;
    width: 540px;
    height: 320px;
    display: flex;
    flex-direction: column;
    box-shadow: 0 10px 24px rgba(0,0,0,.18);
    overflow: hidden;
  }
  .card--back { left: 40px; }
  .card--front { left: 620px; }
  .stripe-green { background: linear-gradient(180deg, var(--green), var(--green-deep)); }
  .stripe-green--top { height: 44px; }
  .stripe-green--bottom { height: 50px; }
  .stripe-grey { height: 30px; background: linear-gradient(180deg, var(--band), var(--band-light)); }
  .panel {
    flex: 1;
    background: linear-gradient(180deg, #f2f2f2, var(--paper) 25%, var(--paper) 80%, #efefef);
    display: flex;
    align-items: center;
  }
  .card--front .panel { justify-content: center; }
  .brand {
    display: flex;
    align-items: center;
    gap: 10px;
  }
  .brand__mark {
    width: 22px;
    height: 22px;
    background: var(--green);
    flex: none;
  }
  .brand__name {
    color: var(--green);
    font-weight: 700;
    font-size: 23px;
    line-height: 1.05;
    text-transform: uppercase;
    letter-spacing: .5px;
  }
  .card--front .brand__name { font-size: 30px; }
  .card--front .brand__mark { width: 28px; height: 28px; }
  .card--back .panel { padding: 0 22px 0 26px; }
  .card--back .brand { width: 226px; }
  .divider {
    width: 1px;
    height: 108px;
    background: var(--ink);
    margin: 0 16px 0 12px;
  }
  .contact__name {
    font-weight: 600;
    font-size: 17px;
    color: var(--ink);
    margin-bottom: 4px;
  }
  .contact__list { list-style: none; font-size: 11px; line-height: 1.45; color: var(--muted); }
  .contact__label { color: var(--green); font-weight: 600; display: inline-block; width: 16px; }
</style>
</head>
<body>
  <section class="card card--back" aria-label="Business card, contact side">
    <div class="stripe-green stripe-green--top"></div>
    <div class="stripe-grey"></div>
    <div class="panel">
      <div class="brand">
        <span class="brand__mark"></span>
        <span class="brand__name">Amber Harbor<br>Supply</span>
      </div>
      <div class="divider"></div>
      <div class="contact">
        <p class="contact__name">Wade Pelham</p>
        <ul class="contact__list">
          <li><span class="contact__label">M:</span>917-555-4820</li>
          <li><span class="contact__label">P:</span>516-555-7164</li>
          <li><span class="contact__label">F:</span>866-555-3291</li>
          <li><span class="contact__label">E:</span>info@amberharborsupply-example.com</li>
          <li><span class="contact__label">W:</span>amberharborsupply-example.com</li>
        </ul>
      </div>
    </div>
    <div class="stripe-grey"></div>
    <div class="stripe-green stripe-green--bottom"></div>
  </section>

  <section class="card card--front" aria-label="Business card, logo side">
    <div class="stripe-green stripe-green--top"></div>
    <div class="stripe-grey"></div>
    <div class="panel">
      <div class="brand">
        <span class="brand__mark"></span>
        <span class="brand__name">Amber Harbor<br>Supply</span>
      </div>
    </div>
    <div class="stripe-grey"></div>
    <div class="stripe-green stripe-green--bottom"></div>
  </section>
</body>
</html>
```